Business Card Design

New business card design

Target Market(s)

Residential & Commercial Property Managers

Industry/Entity Type

Plumbing Services

Contact Information for Business Card

Name - Owen Tredgold, title - Director, Phone Number - 0431 862 507, email - owen@rvb-plumbing.com.au, Company ABN - 73 215 904 386,

Font styles to use
Sans Serif

Colors
0054AA
0677BA
7BADD7
CADEEF
E8F1F8

```html
<!DOCTYPE html>
<html lang="en">
<head>
<meta charset="utf-8">
<title>RVB Plumbing Services – Business Card</title>
<link rel="stylesheet" href="https://fonts.googleapis.com/css2?family=Michroma&family=Poppins:wght@300;400;500;600;700&display=swap">
<style>
  :root {
    --stage: #999999;
    --navy: #002e47;
    --cyan: #1ebdf7;
    --sky: #10a3e6;
    --brand-blue: #0a87c2;
    --ink: #141414;
    --paper-light: #f7f7f7;
    --paper-mid: #e9e9e9;
    --white: #ffffff;
  }
  * { box-sizing: border-box; margin: 0; padding: 0; }
  html, body {
    width: 1004px; height: 1200px; overflow: hidden;
    background: var(--stage);
    font-family: "Poppins", sans-serif;
  }
  .canvas { position: relative; width: 1004px; height: 1200px; }

  .card {
    position: absolute; left: 70px; width: 850px; height: 486px;
    background: var(--navy); overflow: hidden;
    box-shadow: 0 4px 10px rgba(0,0,0,0.35);
  }
  .card--front { top: 78px; }
  .card--back { top: 633px; }

  .edge-bar { position: absolute; background: var(--cyan); }
  .edge-bar--left { left: 0; top: 0; width: 7px; height: 100%; }
  .edge-bar--right { right: 0; top: 0; width: 7px; height: 100%; }
  .edge-tab { position: absolute; background: var(--cyan); }
  .edge-tab--top-left { left: 0; top: 0; width: 19px; height: 148px; border-radius: 0 18px 18px 0 / 0 30px 30px 0; }
  .edge-tab--bottom-right { right: 0; bottom: 0; width: 17px; height: 104px; border-radius: 14px 0 0 14px / 22px 0 0 14px; }

  .brand-name {
    position: absolute; left: 0; width: 100%; text-align: center;
    color: var(--white); font-weight: 300; line-height: 1; white-space: nowrap;
  }
  .brand-name--front { top: 112px; font-size: 96px; letter-spacing: 6px; }
  .brand-tagline {
    position: absolute; left: 0; width: 100%; text-align: center;
    color: var(--white); font-weight: 300; line-height: 1; white-space: nowrap;
  }
  .brand-tagline--front { top: 254px; font-size: 15px; letter-spacing: 13px; }

  .web-line {
    position: absolute; left: 0; top: 346px; width: 100%; text-align: center;
    font-size: 25px; font-weight: 500; letter-spacing: 5px; color: var(--white); white-space: nowrap;
  }
  .web-line .domain { color: var(--sky); font-weight: 700; }

  /* back */
  .back-panel { position: absolute; left: 0; top: 0; width: 353px; height: 100%; background: var(--navy); }
  .back-divider { position: absolute; left: 353px; top: 0; width: 7px; height: 100%; background: var(--cyan); }
  .back-divider-tab { position: absolute; left: 338px; bottom: 0; width: 22px; height: 147px; background: var(--cyan); border-radius: 18px 0 0 18px / 26px 0 0 18px; }
  .back-info {
    position: absolute; left: 360px; top: 0; right: 0; height: 100%;
    background: linear-gradient(135deg, var(--paper-light) 0%, var(--paper-mid) 55%, var(--paper-light) 100%);
  }
  .brand-name--back { left: 0; width: 353px; top: 170px; font-size: 50px; letter-spacing: 3px; }
  .brand-tagline--back { left: 0; width: 353px; top: 250px; font-size: 10px; letter-spacing: 8px; }

  .abn {
    position: absolute; left: 59px; top: 289px; width: 233px; height: 27px;
    border: 1.5px solid var(--cyan); border-radius: 5px; display: flex; overflow: hidden;
  }
  .abn-label { width: 68px; background: var(--cyan); color: var(--navy); font-size: 17px; line-height: 25px; text-align: center; }
  .abn-number { flex: 1; color: var(--white); font-size: 17px; line-height: 25px; text-align: center; font-weight: 500; white-space: nowrap; }

  .person-name {
    position: absolute; left: 57px; top: 106px;
    font-family: "Michroma", sans-serif; font-size: 25px; font-weight: 400; line-height: 1;
    color: var(--brand-blue); white-space: nowrap; -webkit-text-stroke: 0.6px var(--brand-blue);
  }
  .person-title { position: absolute; left: 57px; top: 143px; font-size: 24px; line-height: 1.2; color: var(--ink); white-space: nowrap; }
  .title-rule {
    position: absolute; left: 57px; top: 183px; width: 225px; height: 3px;
    background: linear-gradient(90deg, var(--cyan), rgba(30,189,247,0));
  }

  .icon-rail {
    position: absolute; left: 51px; top: 209px; width: 36px; height: 140px;
    border: 1.5px solid var(--ink); border-radius: 9px;
  }
  .icon {
    position: absolute; left: 58px; width: 23px; height: 23px;
    background: var(--brand-blue); border-radius: 3px;
  }
  .icon svg { display: block; width: 23px; height: 23px; }
  .icon--phone { top: 222px; }
  .icon--mail { top: 267px; }
  .icon--web { top: 312px; }

  .contact { position: absolute; left: 107px; color: var(--ink); line-height: 1; white-space: nowrap; }
  .contact--phone { top: 219px; font-size: 28px; font-weight: 700; }
  .contact--mail { top: 267px; font-size: 20px; }
  .contact--web { top: 312px; font-size: 20px; }
</style>
</head>
<body>
<main class="canvas">

  <section class="card card--front" aria-label="Business card front">
    <div class="edge-bar edge-bar--left"></div>
    <div class="edge-tab edge-tab--top-left"></div>
    <div class="edge-bar edge-bar--right"></div>
    <div class="edge-tab edge-tab--bottom-right"></div>

    <p class="brand-name brand-name--front">rvb</p>
    <p class="brand-tagline brand-tagline--front">plumbing services</p>

    <p class="web-line">www.<span class="domain">rvb-plumbing</span>.com.au</p>
  </section>

  <section class="card card--back" aria-label="Business card back">
    <div class="back-panel"></div>
    <div class="edge-bar edge-bar--left"></div>
    <div class="edge-tab edge-tab--top-left"></div>

    <p class="brand-name brand-name--back">rvb</p>
    <p class="brand-tagline brand-tagline--back">plumbing services</p>

    <div class="abn">
      <span class="abn-label">ABN</span>
      <span class="abn-number">73 215 904 386</span>
    </div>

    <div class="back-info" role="img" aria-label="Light grey background with a subtle geometric diamond texture">
      <h1 class="person-name">OWEN TREDGOLD</h1>
      <p class="person-title">Director</p>
      <div class="title-rule"></div>

      <div class="icon-rail"></div>
      <span class="icon icon--phone">
        <svg viewBox="0 0 24 24" aria-hidden="true"><path fill="#fff" d="M8.2 5.5c.4-.4 1-.4 1.3 0l1.6 2c.3.4.3.9 0 1.2l-1 1c.8 1.6 2 2.8 3.6 3.6l1-1c.3-.3.9-.3 1.2 0l2 1.6c.4.3.4.9 0 1.3l-1.2 1.2c-.6.6-1.5.8-2.3.5-3.4-1.3-6-3.9-7.3-7.3-.3-.8-.1-1.7.5-2.3z"/></svg>
      </span>
      <span class="icon icon--mail">
        <svg viewBox="0 0 24 24" aria-hidden="true"><rect x="5" y="7" width="14" height="10" rx="1" fill="#fff"/><path d="M5.5 7.5 12 12.5l6.5-5M5.5 16.5l5-4.5M18.5 16.5l-5-4.5" stroke="#0a87c2" stroke-width="1.2" fill="none"/></svg>
      </span>
      <span class="icon icon--web">
        <svg viewBox="0 0 24 24" aria-hidden="true"><g fill="none" stroke="#fff" stroke-width="1.3"><circle cx="12" cy="12" r="6.5"/><ellipse cx="12" cy="12" rx="3" ry="6.5"/><path d="M5.5 12h13M6.5 8.8h11M6.5 15.2h11"/></g></svg>
      </span>

      <p class="contact contact--phone">0431 862 507</p>
      <p class="contact contact--mail">owen@rvb-plumbing.com.au</p>
      <p class="contact contact--web">www.rvb-plumbing.com.au</p>
    </div>

    <div class="back-divider"></div>
    <div class="back-divider-tab"></div>
  </section>

</main>
</body>
</html>
```